Non-Fiction Book On Creativity - Cover Design / Physical and E-Book

I am looking for designs for my first book! It's called: Patience Builds Harbors. The subtitle is: 12 Chapters About Gathering Courage, Mending Fences, And Walking A Quiet Road.
It's a series of short lessons and principals on creativity and it will be a Vellora book and a physical book.
I'm really open to any type of designs but have attached some screenshots of other book covers that have a design and style that I like.
Please let me know if you have any questions or need any more information.
Creativity / Self-Help / Personal Development

```html
<!DOCTYPE html>
<html lang="en">
<head>
<meta charset="utf-8">
<title>Patience Builds Harbors — Book Cover</title>
<link rel="stylesheet" href="https://fonts.googleapis.com/css2?family=Chakra+Petch:wght@500;600&display=swap">
<style>
  :root {
    --rose: #e65b7c;
    --tangerine: #f29b38;
    --sky: #8ec4ec;
    --sky-light: #cfe4f6;
    --wall-amber: #f3a83c;
    --wall-coral: #e8647d;
    --paper: #ffffff;
  }
  html, body {
    margin: 0;
    padding: 0;
    width: 800px;
    height: 1200px;
    overflow: hidden;
    background: var(--paper);
  }
  .cover {
    position: relative;
    width: 800px;
    height: 1200px;
    overflow: hidden;
    font-family: "Chakra Petch", "Arial Narrow", sans-serif;
    text-transform: uppercase;
  }
  .cover-backdrop {
    position: absolute;
    inset: 0;
    width: 800px;
    height: 1200px;
  }
  .title-band {
    position: absolute;
    left: 73px;
    width: 634px;
    background: var(--rose);
    color: var(--paper);
    display: flex;
    align-items: center;
    justify-content: center;
    font-weight: 600;
    font-size: 68px;
    letter-spacing: 4px;
    line-height: 1;
  }
  .title-band--top { top: 100px; height: 103px; }
  .title-band--bottom { top: 377px; height: 116px; }
  .title-connector {
    position: absolute;
    top: 270px;
    left: 73px;
    width: 634px;
    text-align: center;
    color: var(--rose);
    font-weight: 600;
    font-size: 68px;
    letter-spacing: 4px;
    line-height: 1;
  }
  .subtitle-panel {
    position: absolute;
    left: 220px;
    top: 780px;
    width: 560px;
    height: 273px;
    box-sizing: border-box;
    padding: 26px 18px 0 17px;
    background: var(--tangerine);
    border-left: 3px solid var(--paper);
    color: var(--paper);
    font-weight: 500;
    font-size: 29px;
    letter-spacing: 1.5px;
    line-height: 50px;
  }
  .subtitle-panel p { margin: 0; }
</style>
</head>
<body>
  <main class="cover">
    <svg class="cover-backdrop" viewBox="0 0 800 1200" role="img"
         aria-label="Upward view of sky and clouds framed by coral and amber architectural walls">
      <defs>
        <linearGradient id="backdrop-tone" x1="0" y1="0" x2="1" y2="1">
          <stop offset="0" stop-color="var(--wall-coral)"/>
          <stop offset="0.3" stop-color="var(--sky)"/>
          <stop offset="0.45" stop-color="var(--sky-light)"/>
          <stop offset="0.65" stop-color="var(--wall-amber)"/>
          <stop offset="1" stop-color="var(--tangerine)"/>
        </linearGradient>
      </defs>
      <rect width="800" height="1200" fill="url(#backdrop-tone)"/>
    </svg>

    <h1 class="book-title">
      <span class="title-band title-band--top">Patience</span>
      <span class="title-connector">Builds</span>
      <span class="title-band title-band--bottom">Harbors</span>
    </h1>

    <div class="subtitle-panel">
      <p>12 Chapters About<br>Gathering Courage,<br>Mending Fences, And<br>Walking A Quiet Road</p>
    </div>
  </main>
</body>
</html>
```